Design Direction Exploration for Brand Deliverables

Here is the link to the finalized logo. If you have a design in this project, please use this version of the logo.

https://files.quorvane.net/get/QmRtPzKdYw

Here's the new web address: tidalharpnarrators.com

I need a business card, a Chainlink Business Banner, a set of slides ("Opening Title slide and the "Thank You" slide), and two social media posts created in accordance with the current brand guidelines for "TidalHarp Narrators | For the Rivers Field". These deliverables should be made within Pintora so I can use them.

Target Market(s)

Professionals in the water sector. TidalHarp is a curated platform that connects water-focused organizations—NGOs, environmental firms, public utilities, and innovators—with exceptional voice actors. Our aim is to elevate the use of voice in storytelling across the water sector, from documentaries and e-learning to product launches and advocacy campaigns. This model puts voice actors first while also responding to a sector with growing communication needs.

Industry/Entity Type

TidalHarp Narrators | For the Rivers Field is the go-to authority in voice talent for the global water industry. Unlike traditional agencies, TidalHarp operates as a highly curated platform, connecting water and environment-focused firms, organizations, innovators, and advocates with exceptional human voice actors who bring clarity, credibility, and impact to their communication. From documentaries and promos to e-learning and product launches, our talent delivers performances at industry rates that engage audiences and elevate the stories shaping the future of water. By focusing exclusively on the water sector, TidalHarp ensures every client gains not only access to world-class voice actors but also a partner who understands the urgency and importance of their mission.

Font styles to use
Other font styles liked:
• See brand guidelines.

Colors

Designer to choose colors to be used in the design.

Requirements
Must have
• The elements of the three page brand guidelines: typeface, color palette, secondary element, and recommendation on photo usage.
Nice to have
• Use the three-page brand guidelines to influence your work. The products should feel high-end, inspirational, modern. If it were a home, it would be featured in Dwelling Quarterly. If it were a specific look, it would be featured in Flair. It's the Valtrane of voice talent. Luxurious, trustworthy, the go-to authority. I like some dimensionality/watermarks.
Should not have
• Cheap looking anything. The brand guidelines is a placeholder that I put together. I will update it based on what design this project yields.

```html
<!DOCTYPE html>
<html lang="en">
<head>
<meta charset="utf-8">
<title>TidalHarp Narrators Business Card</title>
<link rel="stylesheet" href="https://fonts.googleapis.com/css2?family=Figtree:wght@600;800&family=Questrial&display=swap">
<style>
  :root {
    --page-blue: #0f5186;
    --ink-navy: #02334d;
    --river-teal: #0097bf;
    --mist-teal: #8fd3d3;
    --leaf-green: #46b914;
    --paper: #eef5f9;
    --paper-shade: #dceaf2;
  }
  html, body {
    margin: 0;
    padding: 0;
    width: 985px;
    height: 1200px;
    overflow: hidden;
    background: var(--page-blue);
  }
  .canvas {
    position: relative;
    width: 985px;
    height: 1200px;
  }
  .card {
    position: absolute;
    left: 111.5px;
    width: 737px;
    height: 421px;
    overflow: hidden;
  }
  .card--front { top: 110px; }
  .card--back { top: 606px; }

  .droplet-surface {
    position: absolute;
    inset: 0;
    background:
      radial-gradient(ellipse at 20% 25%, #ffffff 0%, rgba(255,255,255,0) 45%),
      radial-gradient(ellipse at 80% 80%, #ffffff 0%, rgba(255,255,255,0) 40%),
      linear-gradient(160deg, var(--paper) 0%, var(--paper-shade) 100%);
  }

  .brand-lockup {
    position: absolute;
    left: 0;
    right: 0;
    top: 140px;
    display: flex;
    flex-direction: column;
    align-items: center;
    gap: 10px;
  }
  .brand-name {
    display: flex;
    align-items: center;
    gap: 16px;
    font-family: "Figtree", sans-serif;
    font-weight: 800;
    font-size: 56px;
    line-height: 1;
    color: var(--ink-navy);
    letter-spacing: -0.5px;
  }
  .brand-mark {
    width: 40px;
    height: 40px;
    border-radius: 50%;
    background: var(--river-teal);
  }
  .brand-tagline {
    font-family: "Figtree", sans-serif;
    font-weight: 600;
    font-size: 26px;
    color: var(--ink-navy);
    padding-left: 56px;
  }

  .accent-bar-left {
    position: absolute;
    left: 0;
    top: 0;
    width: 9px;
    height: 100%;
    background: var(--leaf-green);
  }
  .identity-panel {
    position: absolute;
    left: 9px;
    top: 0;
    width: 340.5px;
    height: 100%;
    background: var(--ink-navy);
  }
  .person-name {
    position: absolute;
    left: 43px;
    top: 136px;
    margin: 0;
    font-family: "Figtree", sans-serif;
    font-weight: 800;
    font-size: 37px;
    line-height: 44px;
    color: #ffffff;
    letter-spacing: -0.5px;
  }
  .person-role {
    position: absolute;
    left: 43px;
    top: 239px;
    margin: 0;
    font-family: "Figtree", sans-serif;
    font-weight: 800;
    font-size: 17.5px;
    line-height: 24px;
    color: var(--mist-teal);
  }
  .contact-tab {
    position: absolute;
    left: 318px;
    top: 95px;
  }
  .contact-list {
    position: absolute;
    left: 396px;
    top: 154px;
    margin: 0;
    padding: 0;
    list-style: none;
    font-family: "Questrial", sans-serif;
    font-size: 17px;
    color: var(--ink-navy);
  }
  .contact-list li {
    height: 57px;
    line-height: 22px;
  }
  .accent-bar-right {
    position: absolute;
    left: 728px;
    top: 276px;
    width: 9px;
    height: 107px;
    background: var(--leaf-green);
  }
</style>
</head>
<body>
<main class="canvas">

  <section class="card card--front" aria-label="Business card front">
    <div class="droplet-surface" role="img" aria-label="Pale blue surface covered in water droplets"></div>
    <div class="brand-lockup">
      <div class="brand-name"><span class="brand-mark"></span>TidalHarp Narrators</div>
      <div class="brand-tagline">For the Rivers Field</div>
    </div>
  </section>

  <section class="card card--back" aria-label="Business card back">
    <div class="droplet-surface" role="img" aria-label="Pale blue surface covered in water droplets"></div>
    <div class="accent-bar-left"></div>
    <div class="identity-panel"></div>
    <h1 class="person-name">MAREN<br>LISLE OKAFOR</h1>
    <p class="person-role">PRINCIPAL VOICE<br>ACTOR &amp; FOUNDER</p>

    <svg class="contact-tab" width="64" height="260" viewBox="0 0 64 260" aria-hidden="true">
      <path d="M0 14 L31 0 L31 16 Z" fill="var(--mist-teal)"/>
      <path d="M0 236 L31 246 L31 260 Z" fill="var(--mist-teal)"/>
      <path d="M0 14 C20 14 31 20 44 30 C58 40 61 50 61 62 L61 194 C61 210 55 218 40 225 C25 232 14 236 0 236 Z" fill="var(--river-teal)"/>
      <!-- phone -->
      <g transform="translate(31 74)" fill="#ffffff">
        <path d="M-6 -10 C-8 -9 -9 -7 -9 -5 C-8 2 -2 9 5 11 C7 11 9 10 10 8 L6 4 L3 6 C0 4 -2 1 -3 -2 L-1 -4 Z"/>
      </g>
      <!-- globe -->
      <g transform="translate(31 125)" fill="none" stroke="#ffffff" stroke-width="2">
        <circle r="11"/>
        <ellipse rx="5" ry="11"/>
        <line x1="-11" y1="0" x2="11" y2="0"/>
        <line x1="0" y1="-11" x2="0" y2="11"/>
        <path d="M-9 -6 H9 M-9 6 H9"/>
      </g>
      <!-- home -->
      <g transform="translate(31 177)" fill="#ffffff">
        <path d="M0 -12 L13 0 L9 0 L9 11 L3 11 L3 4 L-3 4 L-3 11 L-9 11 L-9 0 L-13 0 Z"/>
      </g>
    </svg>

    <ul class="contact-list">
      <li>+123-555-0148</li>
      <li>48 Harbor Lane, Riverton, ST20418</li>
      <li>www.tidalharpnarrators.com</li>
    </ul>
    <div class="accent-bar-right"></div>
  </section>

</main>
</body>
</html>
```